Web Design for couples website

About us:
Duoperks.sg is a new startup website that aims to suggest and promote activities for young couples. The site will feature a blog and a group deals page (i.e Flockbuy).

What we need:
We require a talented designer to design a theme for the website. The design must include at least the following:
1. Logo Design - A logo should be provided along with the website design. The design should match the overall design of the website (or vice versa). The logo should include the words "Duoperks.sg" or "Duoperks". Capitalisation of the alphabets are not critical.

2 - Home / Landing page
The layout of this page should be similar to the standard 2 / 3 column wordpress pages with an image slider on top to feature articles / deals. There should also be a column on the side to include widgets such as social networking and mailing list subscription, etc

3. Deals Listing Page
This page will have a listing of all current group deals, similar to that of Flockbuy. The layout can either have deals listed in 1 or 2 columns.

4. Past Deals Page - See references below

5. Deal Page
Detailed information page for each specific deal. This should include deal image, title, buy button, timer, social media buttons, two column text.

References for deal pages:
www.bargainvale.com.sg
http://www.everyoffernest.com.au/daily-deals
www.totalsavepacific.com
www.hugeswapzo.com

6. General page design for miscellaneous pages like "About", "Contact", etc.

The overall theme of the website should cater to an audience of 18-30 year old young adults. Preferably to have something less colourful and give the overall feel of class. This should cater generally to females but males as well, so less (or no)pink / red would be preferable. But don't let yourself get restricted by these requirements and feel free to let your creative juices flow!
Updates

Hi Designers,

Thank you for your submissions so far. I would like to point out that the deal listing page will only be a sub section of the page.  Would appreciate if priority was given to the main / landing page slider and 2 or 3 columns for articles below.

Other priority would be for the single deal design, where I'm more interested to have more unique buttons such as "buy now" and "time left" .

Also to note, only .PSD design file is required. No coding (HTML / CSS) is necessary and should also be friendly for developers to work with.

Hi Designers,

 
Please submit proposal designs based on requirements on landing page or deal listings page as these would be my main requirements for consideration.

Also, Do try to keep the theme clean and easy on the eyes. Overall, I'm looking for something that is simplistic and/or classy with elegance.

Target Market(s)

18 - 30 years old young adults interested in dating and activities for couples

Industry/Entity Type

Media

Requirements
Must have
• - Logo
- Home
- Deal Page (specific)
- General layout

```html
<!DOCTYPE html>
<html lang="en">
<head>
<meta charset="utf-8">
<title>Duoperks — Today's Deal</title>
<link rel="stylesheet" href="https://fonts.googleapis.com/css2?family=Arimo:wght@400;700&family=Mulish:wght@300;400&display=swap">
<style>
:root{
  --blue:#29a9e1;
  --blue-dark:#1b8fc6;
  --blue-pale:#dff1fb;
  --orange:#f7901e;
  --orange-dark:#e36f0c;
  --ink:#1d1d1d;
  --text:#555;
  --muted:#8a8a8a;
  --nav:#2b2b2b;
  --panel:#f1f1f1;
  --line:#dcdcdc;
  --footer:#ececec;
  --footer-bar:#3a3c3f;
  --green:#6bb42a;
}
*{box-sizing:border-box;margin:0;padding:0}
html,body{width:1200px;height:2186px;overflow:hidden}
body{position:relative;background:#fff;font-family:"Arimo",Arial,sans-serif;color:var(--text);font-size:13px}
.abs{position:absolute}
a{color:inherit;text-decoration:none}

/* header */
.site-header{position:absolute;left:0;top:0;width:1200px;height:149px;background:radial-gradient(ellipse at 30% 10%,#ffffff 0%,#e6f5fc 45%,#c9e8f7 100%)}
.brand{left:127px;top:44px}
.brand-name{font-weight:700;font-size:36px;color:var(--blue);letter-spacing:1px;line-height:1}
.brand-tag{font-weight:700;font-size:13px;color:#222;margin-top:6px;letter-spacing:.3px}
.city{left:451px;top:48px}
.city-name{font-weight:700;font-size:23px;color:#111;display:flex;align-items:center;gap:8px}
.city-name .dot{width:17px;height:17px;border-radius:50%;background:#111;position:relative}
.city-name .dot:after{content:"";position:absolute;left:4px;top:4px;width:6px;height:6px;border-right:2px solid #fff;border-bottom:2px solid #fff;transform:rotate(45deg)}
.city-sub{font-size:13px;color:#222;margin-top:7px}
.city-hint{left:656px;top:86px;font-size:11px;font-weight:700;font-style:italic;color:#222}
.city-arrow{left:628px;top:50px}
.newsletter{left:821px;top:47px}
.newsletter-title{font-size:13px;color:#222}
.newsletter-form{display:flex;margin-top:7px}
.newsletter-input{width:190px;height:28px;border:1px solid #c8c8c8;border-radius:4px 0 0 4px;background:#fff;font-size:11px;color:#888;padding:8px 10px}
.newsletter-send{width:60px;height:28px;background:linear-gradient(#fba23a,var(--orange-dark));color:#fff;font-weight:700;font-size:12px;text-align:center;line-height:28px;border-radius:0 4px 4px 0}

/* nav */
.main-nav{position:absolute;left:0;top:149px;width:1200px;height:45px;background:linear-gradient(#3a3a3a,#1f1f1f);border-bottom:5px solid var(--blue)}
.nav-item{position:absolute;top:15px;color:#fff;font-weight:700;font-size:13px;letter-spacing:.3px}
.nav-item.active:after{content:"";position:absolute;left:36px;top:30px;border:7px solid transparent;border-top-color:var(--blue)}
.nav-signin{position:absolute;left:802px;top:11px;width:67px;height:22px;background:#fff;color:var(--blue);font-size:11px;text-align:center;line-height:22px;clip-path:polygon(8% 0,100% 0,100% 100%,8% 100%,0 50%)}
.nav-util{position:absolute;top:15px;color:#fff;font-size:12px}
.nav-sep{position:absolute;top:13px;width:1px;height:18px;background:#666}
.nav-social{position:absolute;top:7px;width:30px;height:30px;border-radius:50%;background:#fff}

/* hero */
.hero{position:absolute;left:125px;top:226px;width:950px;height:386px;border:1px solid var(--line);border-radius:4px;background:#fff;box-shadow:0 1px 3px rgba(0,0,0,.08)}
.hero-photo{position:absolute;left:449px;top:0;width:500px;height:384px;background:linear-gradient(135deg,#6b4a33 0%,#c89a6a 35%,#e9d3b6 60%,#f5f1ea 78%,#8a6a52 100%);border-radius:0 4px 4px 0}
.hero-wave{position:absolute;left:440px;top:0}
.hero-title{position:absolute;left:33px;top:42px;width:400px;font-family:"Mulish",sans-serif;font-weight:400;font-size:34px;line-height:38px;color:var(--blue)}
.deal-stats{position:absolute;left:12px;top:170px;width:400px}
.stat-row{position:relative;height:28px;font-size:13px;color:#222}
.stat-row.band{background:linear-gradient(90deg,#ccc 0%,#444 20%,#111 60%,rgba(17,17,17,0) 100%);color:#fff}
.stat-row span{position:absolute;top:7px}
.c1{left:24px}.c2{left:112px}.c3{left:173px}.c4{left:254px}
.share{position:absolute;top:7px;width:13px;height:13px;border-radius:2px}
.price-tag{position:absolute;left:-9px;top:270px;width:200px;height:57px;background:linear-gradient(#fba23a,var(--orange-dark));clip-path:polygon(0 0,90% 0,100% 50%,90% 100%,0 100%);color:#fff;font-weight:700;font-size:28px;line-height:57px;padding-left:44px}
.price-tag small{font-size:17px}
.buy-now{position:absolute;left:201px;top:270px;width:201px;height:57px;background:linear-gradient(#4cc3f0,var(--blue-dark));clip-path:polygon(0 0,90% 0,100% 50%,90% 100%,0 100%);color:#fff;font-weight:700;font-size:28px;line-height:57px;padding-left:25px}

/* tabs */
.deal-tabs{position:absolute;left:127px;top:665px;width:670px;height:31px;border-bottom:2px solid var(--blue)}
.tab{position:absolute;top:7px;font-size:15px;color:#555}
.tab.active{left:2px;top:0;width:132px;height:31px;background:linear-gradient(#4cc3f0,var(--blue-dark));color:#fff;text-align:center;line-height:31px;border-radius:4px 4px 0 0}

/* deal cards */
.deal-card{position:absolute;width:200px}
.deal-photo{width:200px;height:148px}
.photo-stones{background:linear-gradient(120deg,#2a2a22 0%,#3d3a30 45%,#6f8a2e 75%,#a6b84a 100%)}
.photo-pizza{background:radial-gradient(circle at 45% 50%,#c23a22 0%,#d8a060 55%,#e9dccb 80%,#b08060 100%)}
.photo-salad{background:linear-gradient(140deg,#1c1c14 0%,#4d7a22 35%,#9bbf4a 55%,#a96840 72%,#222 100%)}
.deal-meta{margin-top:9px;font-size:12px;color:#333;line-height:17px}
.deal-meta div{display:flex}
.deal-meta .k{width:62px}.deal-meta .s{width:34px}
.deal-timer{font-size:12px;color:var(--orange);margin-top:2px}
.view-deal{display:block;margin-top:9px;width:84px;height:24px;background:linear-gradient(#4cc3f0,var(--blue-dark));color:#fff;font-size:12px;text-align:center;line-height:24px;border-radius:2px 0 0 2px;clip-path:polygon(0 0,92% 0,100% 50%,92% 100%,0 100%)}

/* location */
.section-title{position:absolute;font-weight:700;font-size:17px;color:var(--ink)}
.map{position:absolute;left:127px;top:1354px;width:379px;height:274px;background:linear-gradient(135deg,#ece6d6 0%,#e4dfcf 50%,#e9e4d2 100%)}
.venue-pin{position:absolute;left:530px;top:1362px}
.venue{position:absolute;left:583px;top:1360px}
.venue-name{font-weight:700;font-size:27px;line-height:32px;color:var(--ink)}
.venue-lines{margin-top:8px;font-size:14px;line-height:23px;color:var(--muted)}
.venue-lines .hl{color:var(--orange)}
.highlights{position:absolute;left:127px;top:1692px;width:520px;list-style:none}
.highlights li{position:relative;padding-left:24px;font-size:13px;line-height:18px;color:#666;margin-bottom:12px}
.highlights li:before{content:"";position:absolute;left:2px;top:3px;width:11px;height:11px;border-radius:50%;border:1px solid #bbb;background:#f3f3f3}

/* sidebar */
.widget{position:absolute;left:845px;width:228px;background:var(--panel)}
.widget-head{height:28px;background:linear-gradient(#4cc3f0,var(--blue-dark));color:#fff;font-size:15px;line-height:28px;padding-left:14px;position:relative;border-radius:3px 3px 0 0}
.widget-head .more{position:absolute;right:12px;top:0;font-size:12px;text-decoration:underline}
.thumb{position:absolute}
.thumb-man{background:linear-gradient(135deg,#6c5a48,#c9b7a0,#3f3a35)}
.thumb-wine{background:linear-gradient(135deg,#2b1a18,#7a2530,#d9d0c3)}
.thumb-phone{background:linear-gradient(135deg,#1c2a3a,#3d86c8,#9fd0ee)}
.btn-details{position:absolute;width:66px;height:24px;background:linear-gradient(#fba23a,var(--orange-dark));color:#fff;font-size:12px;text-align:center;line-height:24px;clip-path:polygon(0 0,100% 0,100% 75%,50% 100%,0 75%)}
.w-text{position:absolute;left:13px;width:205px;font-size:12.5px;line-height:15px;color:#555}
.stars{position:absolute;display:flex;gap:2px}
.star{width:14px;height:14px;clip-path:polygon(50% 0,61% 35%,98% 35%,68% 57%,79% 91%,50% 70%,21% 91%,32% 57%,2% 35%,39% 35%);background:#f2b51b}
.star.off{background:#c9c9c9}
.fb-box{position:absolute;left:6px;top:36px;width:216px;height:208px;background:#fff;border:1px solid #d8d8d8}
.fb-mark{position:absolute;left:6px;top:8px;width:40px;height:40px;background:var(--blue-pale);color:var(--blue);font-weight:700;font-size:20px;text-align:center;line-height:40px}
.avatar{position:absolute;width:40px;height:40px;background:linear-gradient(135deg,#b8a898,#7b6e64)}
.avatar-name{position:absolute;width:40px;text-align:center;font-size:8px;color:#777}
.about{position:absolute;left:845px;top:1506px;width:228px}
.about h3{font-size:16px;font-weight:400;color:#222}
.about p{margin-top:8px;font-size:13px;line-height:16px;color:#555}

/* footer */
.site-footer{position:absolute;left:0;top:1834px;width:1200px;height:309px;background:var(--footer)}
.f-col{position:absolute;top:98px}
.f-col h4{font-weight:400;font-size:15px;color:var(--blue)}
.f-col ul{list-style:none;margin-top:10px}
.f-col li{font-size:13px;line-height:24px;color:var(--muted)}
.f-sep{position:absolute;top:100px;width:1px;height:150px;background:#d2d2d2}
.f-chirp{position:absolute;left:802px;top:90px;width:250px}
.f-chirp h4{font-weight:400;font-size:15px;color:var(--blue);display:flex;align-items:center;gap:10px}
.f-chirp h4 i{width:30px;height:30px;border-radius:50%;background:#1f2a36;display:block}
.f-chirp p{margin-top:12px;font-size:13px;line-height:16px;color:#666}
.f-chirp .tw-link{margin-top:18px;font-size:12px;color:#555}
.footer-bar{position:absolute;left:0;top:2143px;width:1200px;height:43px;background:var(--footer-bar);color:#fff;font-size:12px}
.card{position:absolute;top:12px;width:33px;height:21px;border-radius:2px;background:#fff}
</style>
</head>
<body>

<header class="site-header">
  <div class="abs brand">
    <div class="brand-name">DUOPERKS</div>
    <div class="brand-tag">A World Group Buy Organisation</div>
  </div>
  <div class="abs city">
    <div class="city-name">SINGAPORE <span class="dot"></span></div>
    <div class="city-sub">Exclusive Deals for Youngs</div>
  </div>
  <svg class="abs city-arrow" width="50" height="34" viewBox="0 0 50 34" aria-hidden="true"><path d="M46 22 C44 6 22 2 6 14" fill="none" stroke="#111" stroke-width="1.6"/><path d="M10 8 L5 14 L12 16" fill="none" stroke="#111" stroke-width="1.6"/></svg>
  <div class="abs city-hint">Find Your City Deal</div>
  <div class="abs newsletter">
    <div class="newsletter-title">Duoperks Daily Deal Newsletter</div>
    <div class="newsletter-form">
      <div class="newsletter-input">Enter Your Email ID</div>
      <div class="newsletter-send">SEND</div>
    </div>
  </div>
</header>

<nav class="main-nav">
  <a class="nav-item active" style="left:127px">TODAY'S DEAL</a>
  <a class="nav-item" style="left:266px">ALL DEALS</a>
  <a class="nav-item" style="left:380px">RECENT DEALS</a>
  <a class="nav-item" style="left:523px">HOW IT WORKS</a>
  <a class="nav-signin">SIGN IN</a>
  <a class="nav-util" style="left:883px">REGISTER</a>
  <span class="nav-sep" style="left:951px"></span>
  <a class="nav-util" style="left:962px">HELP</a>
  <span class="nav-sep" style="left:999px"></span>
  <span class="nav-social" style="left:1008px"></span>
  <span class="nav-social" style="left:1043px"></span>
</nav>

<section class="hero">
  <div class="hero-photo" role="img" aria-label="Glazed croissant pastries on a white plate"></div>
  <svg class="hero-wave" width="40" height="384" viewBox="0 0 40 384" aria-hidden="true">
    <path d="M0 0 H18 C34 20 34 44 20 64 C8 84 8 108 22 128 C36 148 36 172 22 192 C8 212 8 236 22 256 C36 276 36 300 22 320 C8 340 10 364 20 384 H0 Z" fill="#fff"/>
  </svg>
  <h1 class="hero-title">Now 41% attendance increase at Duoperks! 2012.</h1>
  <div class="deal-stats">
    <div class="stat-row"><span class="c1">Value</span><span class="c2">$99</span><span class="c3">Time Left</span><span class="c4">2 days 16:07:39</span></div>
    <div class="stat-row band"><span class="c1">Discount</span><span class="c2">76%</span><span class="c3">Our Love</span>
      <i class="share" style="left:254px;background:#4a78c5"></i><i class="share" style="left:271px;background:#48b8ea"></i><i class="share" style="left:288px;background:#2a82c0"></i><i class="share" style="left:305px;background:#f08a24"></i></div>
    <div class="stat-row"><span class="c1">Saving</span><span class="c2">$75</span><span class="c3">Deals is on</span><span class="c4">11 Bought!</span></div>
  </div>
  <div class="price-tag">$129 <small>ONLY</small></div>
  <a class="buy-now">BUY NOW</a>
</section>

<div class="deal-tabs">
  <span class="tab active">Popular Deals</span>
  <span class="tab" style="left:158px">Insta Deals</span>
  <span class="tab" style="left:278px">Deals By Category</span>
</div>

<!-- deal grid -->
<article class="deal-card" style="left:127px;top:718px">
  <div class="deal-photo photo-stones" role="img" aria-label="Black spa stones with bamboo"></div>
  <div class="deal-meta"><div><span class="k">Deal Value</span><span class="s">:</span>$99.55</div><div><span class="k">Discount</span><span class="s">:</span>45%</div><div><span class="k">You Save</span><span class="s">:</span>$20.22</div></div>
  <div class="deal-timer">0 days 00 hrs 00 min 00 sec</div><a class="view-deal">View Deal</a>
</article>
<article class="deal-card" style="left:357px;top:718px">
  <div class="deal-photo photo-pizza" role="img" aria-label="Tomato pizza"></div>
  <div class="deal-meta"><div><span class="k">Deal Value</span><span class="s">:</span>$99.55</div><div><span class="k">Discount</span><span class="s">:</span>45%</div><div><span class="k">You Save</span><span class="s">:</span>$20.22</div></div>
  <div class="deal-timer">0 days 00 hrs 00 min 00 sec</div><a class="view-deal">View Deal</a>
</article>
<article class="deal-card" style="left:597px;top:718px">
  <div class="deal-photo photo-salad" role="img" aria-label="Grilled meat salad with broccoli"></div>
  <div class="deal-meta"><div><span class="k">Deal Value</span><span class="s">:</span>$99.55</div><div><span class="k">Discount</span><span class="s">:</span>45%</div><div><span class="k">You Save</span><span class="s">:</span>$20.22</div></div>
  <div class="deal-timer">0 days 00 hrs 00 min 00 sec</div><a class="view-deal">View Deal</a>
</article>
<article class="deal-card" style="left:127px;top:1016px">
  <div class="deal-photo photo-stones" role="img" aria-label="Black spa stones with bamboo"></div>
  <div class="deal-meta"><div><span class="k">Deal Value</span><span class="s">:</span>$99.55</div><div><span class="k">Discount</span><span class="s">:</span>45%</div><div><span class="k">You Save</span><span class="s">:</span>$20.22</div></div>
  <div class="deal-timer">0 days 00 hrs 00 min 00 sec</div><a class="view-deal">View Deal</a>
</article>
<article class="deal-card" style="left:357px;top:1016px">
  <div class="deal-photo photo-pizza" role="img" aria-label="Tomato pizza"></div>
  <div class="deal-meta"><div><span class="k">Deal Value</span><span class="s">:</span>$99.55</div><div><span class="k">Discount</span><span class="s">:</span>45%</div><div><span class="k">You Save</span><span class="s">:</span>$20.22</div></div>
  <div class="deal-timer">0 days 00 hrs 00 min 00 sec</div><a class="view-deal">View Deal</a>
</article>
<article class="deal-card" style="left:597px;top:1016px">
  <div class="deal-photo photo-salad" role="img" aria-label="Grilled meat salad with broccoli"></div>
  <div class="deal-meta"><div><span class="k">Deal Value</span><span class="s">:</span>$99.55</div><div><span class="k">Discount</span><span class="s">:</span>45%</div><div><span class="k">You Save</span><span class="s">:</span>$20.22</div></div>
  <div class="deal-timer">0 days 00 hrs 00 min 00 sec</div><a class="view-deal">View Deal</a>
</article>

<h2 class="section-title" style="left:127px;top:1322px">This Deal Location</h2>
<div class="map" role="img" aria-label="Street map of the deal location with three markers"></div>
<svg class="venue-pin" width="36" height="60" viewBox="0 0 36 60" aria-hidden="true">
  <line x1="18" y1="26" x2="18" y2="58" stroke="#999" stroke-width="2"/>
  <circle cx="18" cy="16" r="14" fill="#c62d1f"/><circle cx="13" cy="11" r="4" fill="#e86a5c"/>
</svg>
<div class="venue">
  <div class="venue-name">Lorem Ipsum<br>Resetaurant</div>
  <div class="venue-lines">
    14 Calder Lane<br>Singapore, 10004<br>110-555-0142<br>email : <span class="hl">hello@lorempost.com</span><br>Viste : <span class="hl">website</span>
  </div>
</div>

<h2 class="section-title" style="left:127px;top:1651px">Highlights</h2>
<ul class="highlights">
  <li>Can you handle it? 10 laps driving an actual rear wheel drive rally car on a specially designed course for just $139!</li>
  <li>Plenty of speed and sideways action - the ultimate thrill drive</li>
  <li>Learn how to do it with theory training from qualified, professional instructors. Then put it into action yourself on the course with 10 hot laps</li>
  <li>Can you beat your mates' time?</li>
</ul>

<!-- sidebar -->
<aside class="widget" style="top:667px;height:185px">
  <div class="widget-head">National Deals <span class="more">View all</span></div>
  <div class="thumb thumb-man" style="left:12px;top:41px;width:81px;height:72px" role="img" aria-label="Man working at a desk"></div>
  <div class="abs" style="left:106px;top:42px;font-size:12.5px;line-height:16px;color:#333">
    Value : <b style="color:var(--green)">$50.00</b><br>Discount : <b>25% Off</b><br>Saving : <b>$25.00</b>
  </div>
  <span class="btn-details" style="left:106px;top:89px">Details</span>
  <p class="w-text" style="top:125px">Phasellus pretium, tellus at mollis iaculis, justo ligula semper urna, a elementum purus diam at erat.</p>
</aside>

<aside class="widget" style="top:867px;height:333px">
  <div class="widget-head">Retailers of the Day</div>
  <div class="thumb thumb-wine" style="left:12px;top:41px;width:82px;height:69px" role="img" aria-label="Wine bottle and glass"></div>
  <div class="abs" style="left:111px;top:44px;font-size:12.5px;color:#333">Phasellus pretium</div>
  <div class="stars" style="left:111px;top:66px"><i class="star"></i><i class="star"></i><i class="star"></i><i class="star off"></i><i class="star off"></i></div>
  <span class="btn-details" style="left:111px;top:91px">Details</span>
  <p class="w-text" style="top:122px">Phasellus pretium, tellus at mollis iaculis, justo ligula semper urna, a elementum purus diam at erat.</p>
  <div class="abs" style="left:12px;top:182px;width:204px;height:1px;background:var(--line)"></div>
  <div class="thumb thumb-phone" style="left:12px;top:197px;width:82px;height:66px" role="img" aria-label="Smartphone on a table"></div>
  <div class="abs" style="left:111px;top:200px;font-size:12.5px;color:#333">Phasellus pretium</div>
  <div class="stars" style="left:111px;top:222px"><i class="star"></i><i class="star"></i><i class="star"></i><i class="star off"></i><i class="star off"></i></div>
  <span class="btn-details" style="left:111px;top:244px">Details</span>
  <p class="w-text" style="top:276px">Phasellus pretium, tellus at mollis iaculis, justo ligula semper urna, a elementum purus diam at erat.</p>
</aside>

<aside class="widget" style="top:1222px;height:252px">
  <div class="widget-head">Friendbook</div>
  <div class="fb-box">
    <div class="fb-mark">DP</div>
    <div class="abs" style="left:54px;top:10px;font-size:11px;color:#3b5998">Duoperks <span style="color:#666">on Friendbook</span></div>
    <div class="abs" style="left:54px;top:28px;width:38px;height:16px;border:1px solid #bbb;background:#eee;font-size:10px;line-height:14px;text-align:center;color:#333">Like</div>
    <div class="abs" style="left:0;top:54px;width:214px;height:1px;background:#ddd"></div>
    <div class="abs" style="left:6px;top:60px;font-size:9px;color:#555">58,151 people like Duoperks</div>
    <div class="avatar" style="left:8px;top:76px" role="img" aria-label="Member avatar"></div>
    <div class="avatar" style="left:60px;top:76px" role="img" aria-label="Member avatar"></div>
    <div class="avatar" style="left:112px;top:76px" role="img" aria-label="Member avatar"></div>
    <div class="avatar" style="left:164px;top:76px" role="img" aria-label="Member avatar"></div>
    <div class="avatar-name" style="left:8px;top:118px">Aria</div><div class="avatar-name" style="left:60px;top:118px">Nell</div><div class="avatar-name" style="left:112px;top:118px">Mira</div><div class="avatar-name" style="left:164px;top:118px">Essa</div>
    <div class="avatar" style="left:8px;top:136px" role="img" aria-label="Member avatar"></div>
    <div class="avatar" style="left:60px;top:136px" role="img" aria-label="Member avatar"></div>
    <div class="avatar" style="left:112px;top:136px" role="img" aria-label="Member avatar"></div>
    <div class="avatar" style="left:164px;top:136px" role="img" aria-label="Member avatar"></div>
    <div class="avatar-name" style="left:8px;top:178px">Lina</div><div class="avatar-name" style="left:60px;top:178px">Tove</div><div class="avatar-name" style="left:112px;top:178px">Bree</div><div class="avatar-name" style="left:164px;top:178px">Dax</div>
  </div>
</aside>

<section class="about">
  <h3>About Duoperks</h3>
  <p>Lorem ipsum dolor sit amet, consectetur adipiscing elit. Phasellus et est velit, eget viverra lectus. Pellentesque vitae lacinia odio. Curabitur leo augue, auctor quis commodo eu, faucibus eget tellus. Sed nisi sapien, malesuada sed ullamcorper quis, molestie sed elit.</p>
</section>

<footer class="site-footer">
  <div class="f-col" style="left:127px"><h4>Company</h4><ul><li>Home</li><li>About Us</li><li>Reviews</li><li>Career</li><li>FAQ</li><li>Terms of Use</li></ul></div>
  <span class="f-sep" style="left:279px"></span>
  <div class="f-col" style="left:324px"><h4>Duoperks General</h4><ul><li>Suggest a Business</li><li>Business Owners</li><li>Get Featured</li></ul></div>
  <span class="f-sep" style="left:514px"></span>
  <div class="f-col" style="left:560px"><h4>Duoperks Support</h4><ul><li>Contact Us</li><li>Help</li><li>Friendbook</li><li>Chirper</li></ul></div>
  <span class="f-sep" style="left:768px"></span>
  <div class="f-chirp">
    <h4><i></i>Chirper Duoperks</h4>
    <p>Lorem ipsum dolor sit amet, consectetur adipiscing elit. Phasellus et est velit, eget viverra lectus. Pellentesque vitae lacinia odio. Curabitur leo augue, auctor quis commodo eu, faucibus eget tellus.</p>
    <div class="tw-link">http://dp.link/r7Qx2m &nbsp;|&nbsp; 2hour ago</div>
  </div>
</footer>
<div class="footer-bar">
  <span class="abs" style="left:127px;top:15px">All right reseved with Duoperks © copyright 2012</span>
  <span class="abs" style="left:754px;top:15px">Payment Options</span>
  <span class="card" style="left:872px;background:#cfe3f3"></span>
  <span class="card" style="left:912px"></span>
  <span class="card" style="left:952px;background:#e8eef8"></span>
  <span class="card" style="left:992px"></span>
  <span class="card" style="left:1032px;background:#e6eefa"></span>
</div>

</body>
</html>
```